'Vessel types, Demand, Supply & Disruptions - what's currently driving the bulk shipping

This is required for a talk that needs to cover the following matters

the difference between small, handysize, handymax, panamax, capesize, and very large bulk carriers, how the trade differs, self loading/unloading etc as an intro to the dry bulk trade and what's currently driving the bulk shipping markets.

The below is an initial breakdown on the slides but not finalised

There will need to be an additional slide on the importance of China for the dry bulk trades

Slide 1: Introduction

Welcome and brief overview of dry bulk shipping
Importance in global trade and economy
Slide 2: Types of Dry Bulk Vessels

Capesize: 100,000-400,000 DWT
Panamax: 60,000-100,000 DWT
Supramax: 45,000-60,000 DWT
Handysize: 15,000-45,000 DWT
Description and key features of each vessel type
Slide 3: Vessel Characteristics

Holds and hatches
Draft, beam, and length
Cargo handling equipment
Engine types and power
Slide 4: Routing in Dry Bulk Shipping

Major shipping routes (e.g., Cape of Good Hope, Panama Canal)
Factors influencing routing decisions (e.g., weather, fuel costs)
Strategic chokepoints and canals
Slide 5: Fixing and Chartering

Voyage Charter
Owner's responsibility
Charterer's responsibility
Time Charter
Bareboat Charter
Spot and long-term contracts
Slide 6: Key Charter Party (CP) Terms

Laytime and demurrage
Freight rates
Notice of Readiness (NOR)
Cargo quantities and quality
Ballast bonus
Slide 7: Current Disruptions in Dry Bulk Shipping

Impact of geopolitical events (e.g., trade tensions, conflicts) on shipping lanes
Effects of economic downturns (e.g., COVID-19 pandemic) on demand and supply chains
Environmental regulations affecting vessel operations
Port congestion and delays
Slide 8: Market Trends and Innovations

Technological advancements in vessel design (e.g., eco-friendly propulsion systems, fuel efficiency)
Digitalization and smart shipping solutions
Sustainability initiatives in the industry (e.g., ballast water treatment, emissions reduction)
Slide 9: Mitigation Strategies for Disruptions

Diversification of trading routes and markets
Investment in fleet optimization and efficiency measures
Collaboration with industry partners and stakeholders to address common challenges
Continuous monitoring and adaptation to changing market conditions
Slide 10: Case Study

Example of a recent disruption and its impact on dry bulk shipping operations
Lessons learned and strategies employed to mitigate the effects
Slide 11: Future Outlook

Anticipated trends and challenges in the dry bulk shipping industry
Opportunities for innovation and growth
Importance of sustainability and resilience in shaping the future of the industry
Slide 12: Conclusion

Recap of key points
Call to action for stakeholders to collaborate and innovate for a sustainable and resilient dry bulk shipping industry
Slide 13: Q&A

```html
<!DOCTYPE html>
<html lang="en">
<head>
<meta charset="utf-8">
<title>Bulk Shipping – Vessel types, Demand, Supply &amp; Disruptions</title>
<link href="https://fonts.googleapis.com/css2?family=Poppins:wght@500;600;700&family=Roboto:wght@400;500&display=swap" rel="stylesheet">
<style>
  :root {
    --navy: #154180;
    --navy-deep: #0f3670;
    --gold: #dba734;
    --cream: #f7eedb;
    --ink: #262626;
    --muted: #3b3b3b;
    --band: #e6eaf0;
    --canvas: #e4e4e4;
    --white: #ffffff;
  }
  * { margin: 0; padding: 0; box-sizing: border-box; }
  html, body { width: 1200px; height: 3976px; overflow: hidden; }
  body { background: var(--canvas); font-family: "Roboto", sans-serif; color: var(--ink); position: relative; }

  .slide { position: absolute; left: 85px; width: 1031px; height: 580px; background: var(--white); overflow: hidden; }
  .slide--cover { top: 93px; }
  .slide--intro { top: 735px; }
  .slide--types { top: 1377px; }
  .slide--traits { top: 2019px; }
  .slide--charter { top: 2661px; }
  .slide--mitigation { top: 3303px; }

  .slide-header { position: absolute; top: 0; left: 0; width: 1031px; height: 76px; }
  .slide-header svg { position: absolute; inset: 0; }
  .slide-header__title { position: absolute; left: 60px; top: 10px; font-family: "Poppins", sans-serif; font-weight: 600; font-size: 32px; color: var(--white); }

  .heading { font-family: "Poppins", sans-serif; font-weight: 600; font-size: 40px; color: var(--ink); line-height: 1.2; }
  .heading--center { position: absolute; left: 0; right: 0; text-align: center; }

  /* Cover */
  .cover-art { position: absolute; inset: 0; }
  .cover-title { position: absolute; left: 120px; right: 120px; top: 158px; text-align: center; font-family: "Poppins", sans-serif; font-weight: 600; font-size: 40px; line-height: 57px; color: var(--white); }
  .cover-subtitle { position: absolute; left: 0; right: 0; top: 466px; text-align: center; font-family: "Poppins", sans-serif; font-weight: 600; font-size: 40px; color: var(--ink); }

  /* Intro */
  .intro-heading { position: absolute; left: 62px; top: 184px; }
  .intro-text { position: absolute; left: 64px; top: 268px; width: 420px; font-size: 25px; line-height: 41px; color: var(--ink); }
  .intro-photo { position: absolute; left: 500px; top: 131px; }

  /* Types */
  .types-heading { top: 98px; }
  .vessel { position: absolute; top: 180px; width: 220px; text-align: center; }
  .vessel__ring { width: 150px; height: 150px; margin: 0 auto; border-radius: 50%; background: #e9edf2; padding: 8px; }
  .vessel__photo { width: 134px; height: 134px; border-radius: 50%; }
  .vessel__name { margin-top: 10px; font-family: "Poppins", sans-serif; font-weight: 600; font-size: 21px; color: var(--ink); }
  .vessel__dwt { margin-top: 4px; font-size: 13px; font-weight: 500; color: var(--navy); }
  .vessel__desc { margin-top: 14px; font-size: 12.5px; line-height: 19px; color: var(--muted); padding: 0 18px; }
  .types-note { position: absolute; left: 95px; right: 95px; top: 500px; text-align: center; font-size: 12px; line-height: 19px; color: var(--muted); }

  /* Characteristics */
  .traits-deco { position: absolute; left: 632px; top: 303px; width: 480px; height: 480px; border-radius: 50%; background: #f1f3f7; }
  .traits-ring { position: absolute; left: 48px; top: 118px; width: 422px; height: 422px; border-radius: 50%; background: var(--cream); }
  .traits-photo { position: absolute; left: 74px; top: 144px; width: 370px; height: 370px; border-radius: 50%; }
  .traits-heading { position: absolute; left: 517px; top: 158px; }
  .check-list { list-style: none; position: absolute; }
  .check-list li { position: relative; padding-left: 35px; }
  .check-list .tick { position: absolute; left: 0; }
  .traits-list { left: 515px; top: 238px; }
  .traits-list li { font-size: 19px; font-weight: 500; height: 73.5px; line-height: 30px; color: var(--ink); }
  .traits-list .tick { top: 7px; }

  /* Chartering */
  .charter-heading { top: 160px; }
  .charter-band { position: absolute; left: 0; right: 0; top: 301px; height: 62px; background: var(--band); }
  .charter-item { position: absolute; top: 269px; width: 160px; text-align: center; }
  .charter-item__ring { width: 126px; height: 126px; margin: 0 auto; border-radius: 50%; background: #f4f5f8; padding: 9px; }
  .charter-item__icon { width: 108px; height: 108px; border-radius: 50%; display: flex; align-items: center; justify-content: center; }
  .charter-item__icon--navy { background: var(--navy); }
  .charter-item__icon--gold { background: var(--gold); }
  .charter-item__label { margin-top: 22px; font-size: 15px; font-weight: 500; line-height: 20px; color: var(--ink); }

  /* Mitigation */
  .mitigation-heading { position: absolute; left: 62px; top: 146px; line-height: 49px; }
  .mitigation-list { left: 60px; top: 256px; width: 480px; }
  .mitigation-list li { font-size: 18px; line-height: 28px; color: var(--ink); margin-bottom: 18px; }
  .mitigation-list .tick { top: 6px; }
  .mitigation-photo { position: absolute; left: 585px; top: 151px; width: 383px; height: 374px; }
</style>
</head>
<body>

<!-- Cover -->
<section class="slide slide--cover">
  <svg class="cover-art" width="1031" height="580" viewBox="0 0 1031 580">
    <defs>
      <linearGradient id="coverSea" x1="0" y1="0" x2="1" y2="1">
        <stop offset="0" stop-color="#1a4887"/>
        <stop offset="0.5" stop-color="#1b4a85"/>
        <stop offset="1" stop-color="#143e7c"/>
      </linearGradient>
    </defs>
    <rect width="1031" height="580" fill="url(#coverSea)" role="img" aria-label="Aerial photo of a bulk carrier at sea, tinted navy"/>
    <path d="M0 500 Q515 330 1031 500 L1031 580 L0 580 Z" fill="var(--gold)"/>
    <path d="M0 506 Q515 365 1031 514 L1031 580 L0 580 Z" fill="var(--white)"/>
  </svg>
  <h1 class="cover-title">Vessel types, Demand, Supply &amp; Disruptions - what's currently driving the bulk shipping.</h1>
  <p class="cover-subtitle">Bulk Shipping</p>
</section>

<!-- Introduction -->
<section class="slide slide--intro">
  <header class="slide-header">
    <svg width="1031" height="76" viewBox="0 0 1031 76">
      <polygon points="0,0 872,0 838,62 0,62" fill="var(--navy)"/>
      <polygon points="872,0 1031,0 1031,62 838,62" fill="var(--gold)"/>
      <polygon points="0,62 548,62 540,74 0,74" fill="var(--band)"/>
    </svg>
    <h2 class="slide-header__title">Bulk Shipping</h2>
  </header>
  <h3 class="heading intro-heading">Introduction</h3>
  <p class="intro-text">Welcome and brief overview of dry bulk shipping<br>Importance in global trade and economy</p>
  <svg class="intro-photo" width="531" height="380" viewBox="0 0 531 380">
    <defs>
      <linearGradient id="introShip" x1="0" y1="0" x2="0" y2="1">
        <stop offset="0" stop-color="#7f9fbe"/>
        <stop offset="0.5" stop-color="#b86a4e"/>
        <stop offset="1" stop-color="#4f8aa0"/>
      </linearGradient>
    </defs>
    <polygon points="48,0 531,0 531,380 0,380" fill="var(--cream)"/>
    <polygon points="60,0 531,0 531,370 12,370" fill="url(#introShip)" role="img" aria-label="Photo of a large cargo ship loaded with containers on calm water"/>
  </svg>
</section>

<!-- Types of Dry Bulk Vessels -->
<section class="slide slide--types">
  <header class="slide-header">
    <svg width="1031" height="76" viewBox="0 0 1031 76">
      <polygon points="0,0 872,0 838,62 0,62" fill="var(--navy)"/>
      <polygon points="872,0 1031,0 1031,62 838,62" fill="var(--gold)"/>
      <polygon points="0,62 548,62 540,74 0,74" fill="var(--band)"/>
    </svg>
    <h2 class="slide-header__title">Bulk Shipping</h2>
  </header>
  <h3 class="heading heading--center types-heading">Types of Dry Bulk Vessels</h3>

  <div class="vessel" style="left:37px">
    <div class="vessel__ring"><div class="vessel__photo" role="img" aria-label="Photo of a Capesize bulk carrier at a loading port" style="background:radial-gradient(circle at 40% 40%,#c98a46,#5b4030)"></div></div>
    <p class="vessel__name">Capesize</p>
    <p class="vessel__dwt">100,000-400,000 DWT</p>
    <p class="vessel__desc">Too large for Panama, trades ore and coal.</p>
  </div>
  <div class="vessel" style="left:278px">
    <div class="vessel__ring"><div class="vessel__photo" role="img" aria-label="Photo of a Panamax vessel under way" style="background:radial-gradient(circle at 50% 40%,#a9c4dc,#2f5f86)"></div></div>
    <p class="vessel__name">Panamax</p>
    <p class="vessel__dwt">60,000-100,000 DWT</p>
    <p class="vessel__desc">Sized to the old locks, carries grain and coal.</p>
  </div>
  <div class="vessel" style="left:520px">
    <div class="vessel__ring"><div class="vessel__photo" role="img" aria-label="Photo of grain cargo being loaded into a Supramax hold" style="background:radial-gradient(circle at 50% 60%,#e09a3c,#7a3f1e)"></div></div>
    <p class="vessel__name">Supramax</p>
    <p class="vessel__dwt">45,000-60,000 DWT</p>
    <p class="vessel__desc">Geared with own cranes for smaller ports.</p>
  </div>
  <div class="vessel" style="left:762px">
    <div class="vessel__ring"><div class="vessel__photo" role="img" aria-label="Photo of deck cranes on a Handysize bulk carrier" style="background:radial-gradient(circle at 50% 40%,#e6e9ec,#c2715a)"></div></div>
    <p class="vessel__name">Handysize</p>
    <p class="vessel__dwt">15,000-45,000 DWT</p>
    <p class="vessel__desc">Flexible, self-loading, serving minor ports and bulks.</p>
  </div>

  <p class="types-note">Vessel size sets the trade: larger ships win on cost per tonne over long routes, while smaller geared ships reach shallow, minor ports and carry a wider mix of cargo including grain, steel, fertiliser, cement and timber on regional routes.</p>
</section>

<!-- Vessel Characteristics -->
<section class="slide slide--traits">
  <div class="traits-deco"></div>
  <header class="slide-header">
    <svg width="1031" height="76" viewBox="0 0 1031 76">
      <polygon points="0,0 872,0 838,62 0,62" fill="var(--navy)"/>
      <polygon points="872,0 1031,0 1031,62 838,62" fill="var(--gold)"/>
      <polygon points="0,62 548,62 540,74 0,74" fill="var(--band)"/>
    </svg>
    <h2 class="slide-header__title">Bulk Shipping</h2>
  </header>
  <div class="traits-ring"></div>
  <div class="traits-photo" role="img" aria-label="Photo of boxed cargo moving along a warehouse conveyor" style="background:radial-gradient(circle at 50% 45%,#c9b9a4,#6b5140 70%,#3c3a40)"></div>
  <h3 class="heading traits-heading">Vessel Characteristics</h3>
  <ul class="check-list traits-list">
    <li><svg class="tick" width="17" height="17" viewBox="0 0 17 17"><circle cx="8.5" cy="8.5" r="8.5" fill="var(--gold)"/><path d="M4.8 8.7l2.5 2.5 4.9-5" fill="none" stroke="#fff" stroke-width="2"/></svg>Holds and hatches</li>
    <li><svg class="tick" width="17" height="17" viewBox="0 0 17 17"><circle cx="8.5" cy="8.5" r="8.5" fill="var(--gold)"/><path d="M4.8 8.7l2.5 2.5 4.9-5" fill="none" stroke="#fff" stroke-width="2"/></svg>Draft, beam, and length</li>
    <li><svg class="tick" width="17" height="17" viewBox="0 0 17 17"><circle cx="8.5" cy="8.5" r="8.5" fill="var(--gold)"/><path d="M4.8 8.7l2.5 2.5 4.9-5" fill="none" stroke="#fff" stroke-width="2"/></svg>Cargo handling equipment</li>
    <li><svg class="tick" width="17" height="17" viewBox="0 0 17 17"><circle cx="8.5" cy="8.5" r="8.5" fill="var(--gold)"/><path d="M4.8 8.7l2.5 2.5 4.9-5" fill="none" stroke="#fff" stroke-width="2"/></svg>Engine types and power</li>
  </ul>
</section>

<!-- Fixing and Chartering -->
<section class="slide slide--charter">
  <header class="slide-header">
    <svg width="1031" height="76" viewBox="0 0 1031 76">
      <polygon points="0,0 872,0 838,62 0,62" fill="var(--navy)"/>
      <polygon points="872,0 1031,0 1031,62 838,62" fill="var(--gold)"/>
      <polygon points="0,62 548,62 540,74 0,74" fill="var(--band)"/>
    </svg>
    <h2 class="slide-header__title">Bulk Shipping</h2>
  </header>
  <h3 class="heading heading--center charter-heading">Fixing and Chartering</h3>
  <div class="charter-band"></div>

  <div class="charter-item" style="left:40px">
    <div class="charter-item__ring"><div class="charter-item__icon charter-item__icon--navy">
      <svg width="56" height="56" viewBox="0 0 56 56" fill="none" stroke="#fff" stroke-width="2" stroke-linecap="round" stroke-linejoin="round"><path d="M10 18h26l8-6M30 12l-6 12M20 18l-4-6"/><path d="M8 36l10-6 8 4 6-4 14 8"/><path d="M18 40l6 6M24 38l6 6M30 38l6 6"/></svg>
    </div></div>
    <p class="charter-item__label">Voyage Charter</p>
  </div>
  <div class="charter-item" style="left:198px">
    <div class="charter-item__ring"><div class="charter-item__icon charter-item__icon--gold">
      <svg width="56" height="56" viewBox="0 0 56 56" fill="none" stroke="#fff" stroke-width="2" stroke-linecap="round" stroke-linejoin="round"><circle cx="20" cy="12" r="3"/><circle cx="28" cy="12" r="3"/><circle cx="36" cy="12" r="3"/><path d="M16 22h24v8H16z"/><path d="M6 24l4 16 10 8M50 24l-4 16-10 8"/></svg>
    </div></div>
    <p class="charter-item__label">Owner's<br>Responsibility</p>
  </div>
  <div class="charter-item" style="left:357px">
    <div class="charter-item__ring"><div class="charter-item__icon charter-item__icon--navy">
      <svg width="56" height="56" viewBox="0 0 56 56" fill="none" stroke="#fff" stroke-width="2" stroke-linecap="round" stroke-linejoin="round"><circle cx="28" cy="30" r="11"/><path d="M17 30h22M28 19c-5 6-5 16 0 22M28 19c5 6 5 16 0 22"/><path d="M10 22a20 20 0 0 1 14-12M46 38a20 20 0 0 1-14 12"/><path d="M36 10l6 2-2 6M20 50l-6-2 2-6"/></svg>
    </div></div>
    <p class="charter-item__label">Charterer's<br>Responsibility</p>
  </div>
  <div class="charter-item" style="left:514px">
    <div class="charter-item__ring"><div class="charter-item__icon charter-item__icon--gold">
      <svg width="56" height="56" viewBox="0 0 56 56" fill="none" stroke="#fff" stroke-width="2" stroke-linecap="round"><circle cx="28" cy="28" r="20"/><circle cx="28" cy="28" r="15"/><path d="M28 18v10l7 5"/></svg>
    </div></div>
    <p class="charter-item__label">Time Charter</p>
  </div>
  <div class="charter-item" style="left:672px">
    <div class="charter-item__ring"><div class="charter-item__icon charter-item__icon--navy">
      <svg width="56" height="56" viewBox="0 0 56 56" fill="none" stroke="#fff" stroke-width="2" stroke-linecap="round" stroke-linejoin="round"><rect x="20" y="8" width="16" height="8"/><path d="M14 24h28v-8H14z"/><path d="M8 28l20-6 20 6-4 14H12z"/><path d="M8 48c4 2 8 2 10 0 3 2 7 2 10 0 3 2 7 2 10 0 2 2 6 2 10 0"/></svg>
    </div></div>
    <p class="charter-item__label">Bareboat Charter</p>
  </div>
  <div class="charter-item" style="left:829px">
    <div class="charter-item__ring"><div class="charter-item__icon charter-item__icon--gold">
      <svg width="56" height="56" viewBox="0 0 56 56" fill="none" stroke="#fff" stroke-width="2" stroke-linecap="round" stroke-linejoin="round"><path d="M32 8v26M32 10l12 24H32"/><path d="M12 28h16v6H12zM14 22h10v6"/><path d="M6 36h46l-6 10H12z"/></svg>
    </div></div>
    <p class="charter-item__label">Spot and long-<br>term contracts</p>
  </div>
</section>

<!-- Mitigation Strategies -->
<section class="slide slide--mitigation">
  <header class="slide-header">
    <svg width="1031" height="76" viewBox="0 0 1031 76">
      <polygon points="0,0 872,0 838,62 0,62" fill="var(--navy)"/>
      <polygon points="872,0 1031,0 1031,62 838,62" fill="var(--gold)"/>
      <polygon points="0,62 548,62 540,74 0,74" fill="var(--band)"/>
    </svg>
    <h2 class="slide-header__title">Bulk Shipping</h2>
  </header>
  <h3 class="heading mitigation-heading">Mitigation Strategies<br>for Disruptions</h3>
  <ul class="check-list mitigation-list">
    <li><svg class="tick" width="17" height="17" viewBox="0 0 17 17"><circle cx="8.5" cy="8.5" r="8.5" fill="var(--gold)"/><path d="M4.8 8.7l2.5 2.5 4.9-5" fill="none" stroke="#fff" stroke-width="2"/></svg>Diversification of trading routes and markets</li>
    <li><svg class="tick" width="17" height="17" viewBox="0 0 17 17"><circle cx="8.5" cy="8.5" r="8.5" fill="var(--gold)"/><path d="M4.8 8.7l2.5 2.5 4.9-5" fill="none" stroke="#fff" stroke-width="2"/></svg>Investment in fleet optimization and efficiency measures</li>
    <li><svg class="tick" width="17" height="17" viewBox="0 0 17 17"><circle cx="8.5" cy="8.5" r="8.5" fill="var(--gold)"/><path d="M4.8 8.7l2.5 2.5 4.9-5" fill="none" stroke="#fff" stroke-width="2"/></svg>Collaboration with industry partners and stakeholders to address common challenges</li>
    <li><svg class="tick" width="17" height="17" viewBox="0 0 17 17"><circle cx="8.5" cy="8.5" r="8.5" fill="var(--gold)"/><path d="M4.8 8.7l2.5 2.5 4.9-5" fill="none" stroke="#fff" stroke-width="2"/></svg>Continuous monitoring and adaptation to changing market conditions</li>
  </ul>
  <div class="mitigation-photo" role="img" aria-label="Aerial photo of a loaded container ship sailing on deep blue sea" style="background:radial-gradient(ellipse at 55% 45%,#8a6e55 0%,#2f6fa8 35%,#0f3f78 100%)"></div>
</section>

</body>
</html>
```